Bluerock Custom Water Tank

I primarily market the water tanks so want a business care that reflects that. I have attached the water tank logo. You have been working on our water tank so maybe we can use that on the card et. I am leaving as one sided but can be double sided if that works. The information that needs to be on the cards is as follows: Dennis K. Marlow Phone numbers: Office 555-318-4720 Direct 555-260-9134 Mobile 555-482-1657 email address: dennis@fieldgearsupply.example Address P.O. Box 3827 Cedar Hollow, GA 30519 Web Page: www.fieldgearsupply.example. A lot to fit on the card. Thanks

```html
<!DOCTYPE html>
<html lang="en">
<head>
<meta charset="utf-8">
<title>Bluerock Custom Water Tank – Business Card</title>
<link rel="stylesheet" href="https://fonts.googleapis.com/css2?family=Montserrat:wght@400;500;800&display=swap">
<style>
  :root {
    --bg: #e8e8e6;
    --paper: #f7f7f5;
    --ink: #1d1d1f;
    --red: #d8262c;
    --white: #ffffff;
    --back-dark: #1b1b1c;
    --back-mid: #3a3a3c;
  }
  * { box-sizing: border-box; margin: 0; padding: 0; }
  html, body { width: 1200px; height: 801px; overflow: hidden; }
  body {
    background: var(--bg);
    font-family: "Montserrat", sans-serif;
    color: var(--ink);
    position: relative;
  }
  .card {
    position: absolute;
    top: 240px;
    width: 560px;
    height: 320px;
    box-shadow: 0 6px 18px rgba(0,0,0,0.12);
    overflow: hidden;
  }
  .card--front { left: 30px; background: var(--paper); }
  .card--back  { left: 610px; background: var(--back-dark); }

  .brand {
    position: absolute;
    top: 38px;
    right: 40px;
    display: flex;
    align-items: center;
    gap: 10px;
  }
  .brand__mark { width: 18px; height: 18px; background: var(--red); }
  .brand__name {
    font-weight: 800;
    font-size: 17px;
    letter-spacing: 0.02em;
    text-transform: uppercase;
    color: var(--ink);
  }

  .address {
    position: absolute;
    top: 150px;
    right: 40px;
    text-align: right;
    font-size: 14px;
    font-style: normal;
    line-height: 1.45;
    letter-spacing: 0.02em;
  }

  .person { position: absolute; left: 40px; top: 108px; }
  .person__name {
    color: var(--red);
    font-weight: 500;
    font-size: 21px;
    text-transform: uppercase;
    letter-spacing: 0.03em;
  }
  .person__title { font-size: 13px; margin-top: 2px; letter-spacing: 0.02em; }

  .contacts { list-style: none; margin-top: 14px; }
  .contacts li {
    display: flex;
    align-items: center;
    gap: 9px;
    font-size: 13px;
    line-height: 19px;
    letter-spacing: 0.02em;
  }
  .contacts svg { width: 12px; height: 12px; flex: none; }

  .band-web {
    position: absolute;
    right: 0;
    top: 232px;
    width: 235px;
    height: 36px;
    background: var(--red);
    clip-path: polygon(12px 0, 100% 0, 100% 100%, 0 100%);
    display: flex;
    align-items: center;
    justify-content: flex-end;
    padding-right: 26px;
    color: var(--white);
    font-size: 14px;
    letter-spacing: 0.02em;
  }
  .band-base {
    position: absolute;
    left: 0;
    top: 268px;
    width: 338px;
    height: 24px;
    background: var(--ink);
    clip-path: polygon(0 0, 100% 0, calc(100% - 10px) 100%, 0 100%);
  }

  .back-texture {
    position: absolute;
    inset: 0;
    background: linear-gradient(135deg, var(--back-dark) 0%, var(--back-mid) 55%, var(--back-dark) 100%);
  }
  .back-brand {
    position: absolute;
    right: 70px;
    top: 150px;
    display: flex;
    align-items: center;
    gap: 8px;
  }
  .back-brand__mark { width: 12px; height: 12px; background: var(--red); }
  .back-brand__name {
    color: var(--red);
    font-weight: 800;
    font-size: 13px;
    text-transform: uppercase;
    letter-spacing: 0.04em;
  }
</style>
</head>
<body>

<section class="card card--front" aria-label="Business card front">
  <div class="brand">
    <span class="brand__mark"></span>
    <span class="brand__name">Bluerock Custom Water Tank</span>
  </div>

  <address class="address">
    P.O. Box 3827<br>
    Cedar Hollow, GA 30519
  </address>

  <div class="person">
    <h1 class="person__name">Dennis K. Marlow</h1>
    <p class="person__title">Managing Director</p>
    <ul class="contacts">
      <li>
        <svg viewBox="0 0 12 12"><circle cx="6" cy="6" r="6" fill="#d8262c"/><path d="M3.5 4.2c0-.5.6-1 1-.8l.6.9-.5.6c.3.7.8 1.2 1.5 1.5l.6-.5.9.6c.2.4-.3 1-.8 1C4.9 7.5 3.5 6.1 3.5 4.2z" fill="#fff"/></svg>
        555-318-4720
      </li>
      <li>
        <svg viewBox="0 0 12 12"><circle cx="6" cy="6" r="6" fill="#d8262c"/><path d="M3.5 4.2c0-.5.6-1 1-.8l.6.9-.5.6c.3.7.8 1.2 1.5 1.5l.6-.5.9.6c.2.4-.3 1-.8 1C4.9 7.5 3.5 6.1 3.5 4.2z" fill="#fff"/></svg>
        555-260-9134
      </li>
      <li>
        <svg viewBox="0 0 12 12"><circle cx="6" cy="6" r="6" fill="#d8262c"/><rect x="4.2" y="2.8" width="3.6" height="6.4" rx="0.6" fill="none" stroke="#fff" stroke-width="0.9"/></svg>
        555-482-1657
      </li>
      <li>
        <svg viewBox="0 0 12 12"><circle cx="6" cy="6" r="6" fill="#d8262c"/><rect x="3.1" y="4" width="5.8" height="4" fill="none" stroke="#fff" stroke-width="0.8"/><path d="M3.1 4 6 6.3 8.9 4" fill="none" stroke="#fff" stroke-width="0.8"/></svg>
        dennis@fieldgearsupply.example
      </li>
    </ul>
  </div>

  <div class="band-web">fieldgearsupply.example</div>
  <div class="band-base"></div>
</section>

<section class="card card--back" aria-label="Business card back">
  <div class="back-texture" role="img" aria-label="Dark embossed repeating pattern of the company tank mark"></div>
  <div class="back-brand">
    <span class="back-brand__mark"></span>
    <span class="back-brand__name">Bluerock</span>
  </div>
</section>

</body>
</html>
```